Dental Lab Delivery Box Design 163x115x97mm

* AI file of the box attached
* Full-Color outside and one color inside
* Return pictures of the 3D design; so we can have a better idea of how it will turn out
* Match Logo Color and Design
* Please find attached Words doc for the wording
* Research the dental lab delivery
* Attached our sister lab dental lab design
*
Updates

Target Market(s)

Dental Office

Industry/Entity Type

Dental Lab

Font styles to use
Serif

Colors
0054AA
0677BA
7BADD7
CADEEF
E8F1F8

Requirements
Must have
• Advance, Clean, and Matched Logo color
Nice to have
• Graphics
Should not have
• Too much words or over advertise

```html
<!DOCTYPE html>
<html lang="en">
<head>
<meta charset="utf-8">
<title>Velora Dental Inc — Delivery Box Dieline</title>
<link href="https://fonts.googleapis.com/css2?family=Montserrat:wght@600&family=Tinos&family=Arimo&display=swap" rel="stylesheet">
<style>
  :root {
    --canvas: #dedede;
    --paper: #ffffff;
    --cut: #e0218a;
    --score: #8a8a8a;
    --brand-deep: #1b56a0;
    --brand-mid: #0677ba;
    --brand-light: #4fa8dc;
    --brand-pale: #cadeef;
    --brand-mist: #e8f1f8;
    --ink: #222222;
  }
  html, body { margin: 0; padding: 0; overflow: hidden; }
  body { width: 1200px; height: 1117px; background: var(--canvas); position: relative; font-family: "Tinos", serif; }
  .dieline { position: absolute; left: 0; top: 0; }
  .panel { position: absolute; box-sizing: border-box; }
  .wordmark { font-family: "Montserrat", sans-serif; font-weight: 600; letter-spacing: 1px; white-space: nowrap; display: flex; align-items: center; gap: 8px; }
  .wordmark .dot { width: 14px; height: 14px; border-radius: 50%; background: currentColor; flex: none; }

  .lid-art { left: 447px; top: 77px; width: 307px; height: 173px;
    background: linear-gradient(120deg, #cfe8f8 0%, #9fd0f1 40%, #4fa8e0 75%, #1d6fc4 100%); }
  .lid-art .wordmark { position: absolute; left: 34px; top: 74px; font-size: 17px; color: var(--brand-deep); }

  .band-left { left: 264px; top: 250px; width: 177px; height: 212px; background: linear-gradient(90deg, #52abdd, #1f62ac); }
  .band-center { left: 441px; top: 250px; width: 318px; height: 212px; background: var(--brand-deep); display: flex; align-items: center; justify-content: center; }
  .band-center .wordmark { font-size: 22px; color: var(--paper); }
  .band-right { left: 759px; top: 250px; width: 177px; height: 212px; background: linear-gradient(90deg, #1f62ac, #52abdd); }

  .end-mark { position: absolute; width: 86px; height: 86px; border-radius: 50%; border: 9px solid var(--brand-light); box-sizing: border-box; }
  .end-left { left: 126px; top: 314px; }
  .end-right { left: 988px; top: 314px; }

  .inner-lid { left: 445px; top: 462px; width: 310px; height: 177px; transform: rotate(180deg); }
  .inner-lid .wordmark { position: absolute; left: 0; right: 0; top: 18px; justify-content: center; font-size: 13px; color: var(--brand-deep); }
  .inner-lid .welcome { position: absolute; left: 0; right: 0; top: 76px; text-align: center; font-size: 7px; color: var(--ink); margin: 0; }
  .inner-lid .story { position: absolute; left: 44px; right: 44px; top: 88px; font-size: 5.4px; line-height: 7px; text-align: justify; color: var(--ink); margin: 0; }

  .photo { left: 452px; top: 639px; width: 296px; height: 215px;
    background: radial-gradient(circle at 30% 35%, #d4d6da 0%, #eeeff1 45%, #fafafa 100%); }
  .photo .wordmark { position: absolute; right: 10px; bottom: 34px; font-size: 19px; color: var(--brand-deep); }

  .base-mark { left: 560px; top: 898px; width: 90px; height: 90px; border-radius: 50%; border: 10px solid var(--brand-deep); }

  .legend { position: absolute; left: 96px; width: 97px; font-family: "Arimo", sans-serif; font-size: 12px; color: var(--ink); text-align: center; }
  .legend span { display: block; padding-bottom: 4px; border-bottom: 1px solid; }
  .legend-cut { top: 956px; } .legend-cut span { border-color: var(--cut); }
  .legend-score { top: 986px; } .legend-score span { border-color: var(--score); }
  .inner-size { position: absolute; left: 63px; top: 1029px; font-family: "Arimo", sans-serif; font-size: 12.5px; letter-spacing: 0.3px; color: var(--ink); }
</style>
</head>
<body>
<svg class="dieline" width="1200" height="1117" viewBox="0 0 1200 1117" aria-hidden="true">
  <g fill="#ffffff" stroke="#e0218a" stroke-width="0.8">
    <!-- lid flaps -->
    <path d="M350 77 H447 V247 H384 L350 229 Z"/>
    <path d="M754 77 H851 V229 L817 247 H754 Z"/>
    <!-- end flaps -->
    <path d="M83 256 H256 V457 H83 V399 H76 V314 H83 Z"/>
    <path d="M256 256 L264 250 V462 L256 457 Z"/>
    <path d="M945 256 H1117 V314 H1124 V399 H1117 V457 H945 Z"/>
    <path d="M936 250 L945 256 V457 L936 462 Z"/>
    <!-- inner lid flaps -->
    <path d="M349 483 L384 466 H445 V636 H349 Z"/>
    <path d="M755 466 H817 L852 483 V636 H755 Z"/>
    <!-- rounded side flaps -->
    <path d="M452 640 L310 675 Q275 688 275 718 V781 Q275 810 310 822 L452 854 Z"/>
    <path d="M748 640 L890 675 Q925 688 925 718 V781 Q925 810 890 822 L748 854 Z"/>
    <!-- curved base flaps -->
    <path d="M445 866 H310 Q279 866 279 900 Q290 1032 445 1032 Z"/>
    <path d="M755 866 H890 Q921 866 921 900 Q910 1032 755 1032 Z"/>
    <!-- main panels -->
    <rect x="445" y="462" width="310" height="177"/>
    <rect x="445" y="854" width="310" height="178"/>
  </g>
  <g fill="none" stroke="#e0218a" stroke-width="0.8">
    <rect x="447" y="77" width="307" height="173"/>
    <rect x="264" y="250" width="672" height="212"/>
    <rect x="442" y="313" width="8" height="86" rx="4"/>
    <rect x="750" y="313" width="8" height="86" rx="4"/>
  </g>
</svg>

<div class="panel lid-art" role="img" aria-label="Bright blue abstract light swirl with a white 3D tooth">
  <div class="wordmark">Velora Dental Inc</div>
</div>

<div class="panel band-left"></div>
<div class="panel band-center"><div class="wordmark"><span class="dot"></span>Velora Dental Inc</div></div>
<div class="panel band-right"></div>

<div class="end-mark end-left"></div>
<div class="end-mark end-right"></div>

<div class="panel inner-lid">
  <div class="wordmark">Velora Dental Inc</div>
  <p class="welcome">Welcome to Velora!</p>
  <p class="story">Headquartered in Riverton Bay, we are a full digital dental lab for all you need. We strive to build excellent relationship and services with our clients, utilize highly experienced technicians and advanced case management systems. Velora stands for care, craft, trust and service. We care for your team as one team. Velora looks forward to building and improving your reputation and bringing more smiles to our services.</p>
</div>

<div class="panel photo" role="img" aria-label="Soft focus photo of a dental lab microscope">
  <div class="wordmark">Velora Dental Inc</div>
</div>

<div class="panel base-mark"></div>

<div class="legend legend-cut"><span>Cut Line</span></div>
<div class="legend legend-score"><span>Score Line</span></div>
<div class="inner-size">Inner size:163x115x97mm</div>
</body>
</html>
```